Professional, Modern and Clean Business Card
Brightvale Grocers & Supply Partners, Inc.
Professional, Modern and Clean Business Card - Food
Creative Brief
Simple
Dorian Whitcombe
71-14 82nd Avenue Maspeth, NY 11492
dorian@brightvalegrocers.example
www.brightvalegrocers.example
We will need 2 business cards, one for myself Dorian Whitcombe and the other Rowan Elkhart. My information is above, for Rowan Elkhart the cell is (214) 555-0193 and the email is row@brightvalegrocers.example, everything else will remain the same.
Be creative with just the logo on the back.

```html
<!DOCTYPE html>
<html lang="en">
<head>
<meta charset="utf-8">
<title>Brightvale Grocers – Business Card</title>
<link href="https://fonts.googleapis.com/css2?family=Montserrat:wght@700;800&family=Open+Sans:wght@400;600;700&display=swap" rel="stylesheet">
<style>
  :root {
    --backdrop: #ececec;
    --card-white: #ffffff;
    --brand-red: #e3222c;
    --brand-red-dark: #c8161f;
    --brand-red-light: #f0393f;
    --leaf-green: #6aa842;
    --leaf-green-dark: #3f7f2a;
    --ink: #4a4a4a;
    --ink-soft: #7a7a7a;
  }
  * { box-sizing: border-box; margin: 0; padding: 0; }
  html, body {
    width: 1200px; height: 939px; overflow: hidden;
    background: var(--backdrop);
    font-family: "Open Sans", Arial, sans-serif;
  }
  .sheet {
    position: relative; width: 1200px; height: 939px;
    display: flex; align-items: center; justify-content: center; gap: 70px;
  }
  .card {
    position: relative; width: 500px; height: 286px; overflow: hidden;
    box-shadow: 0 10px 28px rgba(0,0,0,0.16);
  }
  .card-front { background: var(--card-white); }
  .card-front .swoosh { position: absolute; inset: 0; width: 100%; height: 100%; }
  .front-content { position: relative; padding: 32px 34px; }
  .wordmark {
    font-family: "Montserrat", Arial, sans-serif; font-weight: 800;
    color: var(--brand-red); font-size: 34px; letter-spacing: -0.5px; line-height: 1;
  }
  .holder-name {
    margin-top: 22px; font-size: 15px; font-weight: 700; color: var(--brand-red);
  }
  .holder-title { font-size: 12px; color: var(--ink); margin-top: 2px; }
  .contact-list { list-style: none; margin-top: 14px; }
  .contact-list li {
    display: flex; align-items: center; gap: 7px;
    font-size: 9.5px; color: var(--ink); line-height: 1.75;
  }
  .contact-list svg { width: 9px; height: 9px; flex: none; }
  .card-back {
    background: radial-gradient(ellipse at 50% 45%, var(--brand-red-light) 0%, var(--brand-red) 55%, var(--brand-red-dark) 100%);
    display: flex; align-items: center; justify-content: center;
  }
  .card-back .wordmark { color: var(--card-white); font-size: 46px; }
</style>
</head>
<body>
<main class="sheet">
  <section class="card card-front" aria-label="Business card front">
    <svg class="swoosh" viewBox="0 0 500 286" preserveAspectRatio="none" aria-hidden="true">
      <path d="M500 120 C420 150 330 210 250 286 L500 286 Z" fill="var(--leaf-green)"/>
      <path d="M500 138 C430 175 360 230 300 286 L500 286 Z" fill="var(--leaf-green-dark)"/>
      <path d="M500 150 C440 190 380 240 330 286 L500 286 Z" fill="var(--brand-red)"/>
    </svg>
    <div class="front-content">
      <div class="wordmark">Brightvale</div>
      <p class="holder-name">Dorian Whitcombe</p>
      <p class="holder-title">Consultant</p>
      <ul class="contact-list">
        <li><svg viewBox="0 0 10 10"><path d="M5 0a3.5 3.5 0 0 0-3.5 3.5C1.5 6 5 10 5 10s3.5-4 3.5-6.5A3.5 3.5 0 0 0 5 0zm0 5a1.5 1.5 0 1 1 0-3 1.5 1.5 0 0 1 0 3z" fill="var(--brand-red)"/></svg>71-14 82nd Avenue Maspeth, NY 11492</li>
        <li><svg viewBox="0 0 10 10"><path d="M2 0.5l2 2-1 1.3c.6 1.3 1.6 2.3 2.9 2.9l1.3-1 2 2-1.4 1.8C4.5 9.2.8 5.5.5 1.9z" fill="var(--brand-red)"/></svg>(214) 555-0193</li>
        <li><svg viewBox="0 0 10 10"><path d="M2 0.5l2 2-1 1.3c.6 1.3 1.6 2.3 2.9 2.9l1.3-1 2 2-1.4 1.8C4.5 9.2.8 5.5.5 1.9z" fill="var(--brand-red)"/></svg>(214) 555-0148</li>
        <li><svg viewBox="0 0 10 10"><rect x="0.5" y="2" width="9" height="6" fill="var(--brand-red)"/><path d="M0.8 2.3L5 5.5l4.2-3.2" stroke="#fff" stroke-width="0.8" fill="none"/></svg>dorian@brightvalegrocers.example</li>
        <li><svg viewBox="0 0 10 10"><circle cx="5" cy="5" r="4.5" fill="var(--brand-red)"/><path d="M0.5 5h9M5 0.5c-2 2.5-2 6.5 0 9M5 0.5c2 2.5 2 6.5 0 9" stroke="#fff" stroke-width="0.6" fill="none"/></svg>www.brightvalegrocers.example</li>
      </ul>
    </div>
  </section>

  <section class="card card-back" aria-label="Business card back">
    <div class="wordmark">Brightvale</div>
  </section>
</main>
</body>
</html>
```